Vexaroll needs a newsletter to introduce our new test - Helix Body Balance

I need a newsletter or email design to introduce a new test that my company has to offer called Helix Body Balance. We are launching this genetic test to fitness centers, nutritionists, high end gyms, personal trainers and others. The genetic test looks at 5 genetic markers that are key to how each individual processes nutrients, carbohydrates etc and then provides a comprehensive report for the individual on specific diet plans, exercise regimens and their genetic results. The newsletter should be an exciting announcement of this new test and one that can easily be used via email or via attachments. I have attached some files which provide much more detail. The final design should communicate an opportunity for these potential customers to increase revenue, provide their members with an extraordinary personalized genetic test and to provide a value add to their current offerings.
Updates
Hi,
I forgot to upload a one page marketing piece that i had created as well as the logo for vexaroll. Happy to provide just not sure how to upload them into the project
Target Market(s)
fitness centers, high end gyms, nutritionists, dieticians, personal trainers, health coaches
Colors
Designer to choose colors to be used in the design.
Look and feel
Each slider illustrates characteristics of the customer's brand and the style your logo design should communicate.

```html
<!DOCTYPE html>
<html lang="en">
<head>
<meta charset="utf-8">
<title>Vexaroll – Helix Body Balance Newsletter</title>
<link href="https://fonts.googleapis.com/css2?family=Montserrat:ital,wght@0,400;0,500;0,600;0,700;1,500&display=swap" rel="stylesheet">
<style>
:root{
  --teal:#16b3aa;
  --teal-text:#19aba3;
  --blue:#1a7fae;
  --dark:#3f3f3f;
  --ink:#2f2f2f;
  --muted:#555;
  --white:#fff;
  --line:#d7d7d7;
}
*{box-sizing:border-box;margin:0;padding:0}
html,body{width:1200px;height:3341px;overflow:hidden}
body{position:relative;background:#fff;font-family:"Montserrat",sans-serif;color:var(--ink)}
.backdrop{position:absolute;left:0;top:0;width:1200px;height:272px;background:linear-gradient(180deg,#10b4ad 0%,#1593b3 100%)}
.sheet{position:absolute;top:127px;width:521px;background:#fff;border:1px solid var(--line)}
.sheet--full{left:67px;height:3138px}
.sheet--short{left:632px;height:1473px}

/* header */
.masthead{position:relative;height:52px}
.masthead__mail,.masthead__call{position:absolute;top:20px;display:flex;align-items:center;gap:8px;font-size:13px;color:var(--teal-text)}
.masthead__mail{left:43px}
.masthead__call{right:44px;font-size:12px;font-weight:600;top:22px}
.masthead__mail svg{width:21px;height:15px}
.masthead__call svg{width:16px;height:16px}
.brand{position:absolute;left:50%;top:0;transform:translateX(-50%);width:100px;height:80px;background:#fff;z-index:2;display:flex;flex-direction:column;align-items:center;justify-content:center;gap:6px;border-radius:0 0 4px 4px}
.brand__dot{width:30px;height:30px;border-radius:50%;background:var(--teal)}
.brand__name{font-size:14px;font-weight:600;color:#1d3d7a}

/* hero */
.hero{position:relative;height:213px;background:linear-gradient(120deg,#7b7b76 0%,#c9c8c2 35%,#eceae4 60%,#a6a6a0 100%);display:flex;align-items:center;justify-content:center}
.hero__title{font-size:30px;font-weight:600;color:#fff;text-shadow:0 1px 3px rgba(0,0,0,.45);letter-spacing:.3px}

/* obesity */
.factors{position:relative;height:270px}
.factors__title{position:absolute;top:28px;width:100%;text-align:center;font-size:16px;font-weight:500}
.factors__title span{color:var(--teal-text)}
.pie{position:absolute;left:97px;top:86px;width:112px;height:112px}
.pie__label{position:absolute;font-size:9px;font-style:italic;color:#333}
.pie__label--non{left:31px;top:88px}
.pie__label--gen{left:36px;top:123px}
.checklist{position:absolute;left:250px;top:68px;list-style:none}
.checklist li{display:flex;align-items:center;gap:9px;height:25px;font-size:13px;color:#444}
.checklist svg{width:17px;height:17px;flex:none}
.factors__note{position:absolute;top:217px;width:100%;text-align:center;font-size:11.5px;font-weight:500}

/* teal banner */
.markers{position:relative;height:114px;background:linear-gradient(180deg,var(--teal) 0%,var(--blue) 100%);color:#fff}
.markers__figure{position:absolute;left:8px;top:4px;width:120px;height:106px;background:radial-gradient(ellipse at center,rgba(255,255,255,.85) 0%,rgba(255,255,255,.35) 55%,rgba(255,255,255,0) 72%)}
.markers__text{position:absolute;left:112px;top:24px;width:395px;font-size:11px;line-height:22px}

/* panel */
.panel{position:relative;height:336px}
.panel__title{position:absolute;top:33px;width:100%;text-align:center;font-size:15.5px;font-weight:500;letter-spacing:.3px}
.panel__figure{position:absolute;left:225px;top:68px;width:72px;height:182px;border-radius:36px 36px 10px 10px;background:linear-gradient(180deg,#f3c9b5 0%,#e0443c 30%,#555 60%,#9a9a9a 100%)}
.gene-dot{position:absolute;width:44px;height:44px;border-radius:50%;background:var(--teal);box-shadow:2px 2px 0 #0e8c85;color:#fff;font-size:12px;font-weight:500;display:flex;align-items:center;justify-content:center}
.gene-dot--mc4r{left:165px;top:90px}
.gene-dot--fto{left:301px;top:90px}
.gene-dot--fabp2{left:165px;top:177px}
.gene-dot--adrb2{left:301px;top:177px}
.gene-dot--sh2b1{left:236px;top:239px}
.panel__label{position:absolute;font-size:12.5px;line-height:18px;color:#444}
.panel__label--meta{left:18px;top:103px}
.panel__label--appetite{left:353px;top:103px}
.panel__label--fat{left:18px;top:189px}
.panel__label--carb{left:353px;top:189px}
.panel__caption{position:absolute;top:299px;width:100%;text-align:center;font-size:12.5px;color:#444}

/* benefits */
.benefits{position:relative;height:157px;background:linear-gradient(180deg,var(--teal) 0%,var(--blue) 100%);color:#fff}
.benefits__title{position:absolute;left:22px;top:16px;font-size:16px;font-weight:600}
.benefits__sub{position:absolute;left:22px;top:39px;font-size:13.5px}
.benefits__list{position:absolute;left:22px;top:64px;list-style:none;width:320px}
.benefits__list li{display:flex;gap:14px;font-size:12.5px;line-height:18px;margin-bottom:16px}
.benefits__list svg{width:17px;height:17px;flex:none;margin-top:2px}
.benefits__photo{position:absolute;right:0;top:0;width:186px;height:157px;background:linear-gradient(90deg,rgba(255,255,255,0) 0%,#a5a0c4 35%,#8a7a6a 70%,#5a6f8a 100%)}

/* personalize */
.invite{height:113px;text-align:center;padding-top:28px}
.invite__lead{font-size:16px;line-height:22px}
.invite__small{margin-top:12px;font-size:12px;font-weight:500}

/* gene table */
.gene-table{margin:0 19px;width:481px;border-collapse:collapse;color:#fff;font-size:10px;line-height:17.5px}
.gene-table th{height:43px;background:var(--teal);text-align:left;font-size:12.5px;font-weight:600;padding-left:18px;border-bottom:4px solid #fff}
.gene-table td{vertical-align:top;padding-top:20px;border-bottom:4px solid #fff}
.gene-table tr.is-teal td{background:var(--teal)}
.gene-table tr.is-dark td{background:var(--dark)}
.gene-table .col-gene{width:82px;font-size:12.5px;font-weight:600;padding-left:18px}
.gene-table .col-type{width:193px;padding-right:24px}
.gene-table .col-plan{padding-right:10px}
.gene-table th.col-type,.gene-table th.col-plan{padding-left:0}
.gene-table th.col-type{padding-left:6px}
.col-type{padding-left:6px}
.plan__label{font-weight:700}
.plan__ex{display:block;margin-top:10px;font-size:13px;font-weight:600}
.plan__ex-text{display:block;padding-left:3px;font-size:9.5px}
.row-fto td{height:262px}
.row-mc4r td{height:260px}
.row-fabp2 td{height:370px}
.row-adrb2 td{height:352px}
.row-sh2b1 td{height:355px}
.row-mc4r .col-plan .plan__body{font-weight:600}

/* closing */
.closing{position:relative;height:204px}
.sheet--short .closing{height:218px}
.closing__quote{position:absolute;top:12px;width:100%;text-align:center;font-size:21px;font-style:italic;font-weight:500;color:var(--teal-text)}
.closing__bike{position:absolute;left:56px;top:50px;width:84px;height:150px;border-radius:10px;background:linear-gradient(180deg,#e85a4a 0%,#cfcfcf 45%,#555 100%)}
.closing__text{position:absolute;left:183px;top:78px;font-size:16.5px;line-height:23px}
</style>
</head>
<body>
<svg width="0" height="0" style="position:absolute" aria-hidden="true">
  <defs>
    <symbol id="tick" viewBox="0 0 20 20"><path d="M17 8.5A7.5 7.5 0 1 1 12.5 3" fill="none" stroke="currentColor" stroke-width="1.6" stroke-linecap="round"/><path d="M6.5 9.5l3 3L18 4" fill="none" stroke="currentColor" stroke-width="1.8" stroke-linecap="round" stroke-linejoin="round"/></symbol>
    <symbol id="mail" viewBox="0 0 22 16"><rect x="1" y="1" width="20" height="14" fill="none" stroke="currentColor" stroke-width="1.8"/><path d="M1 1l10 8 10-8M1 15l7-6M21 15l-7-6" fill="none" stroke="currentColor" stroke-width="1.6"/></symbol>
    <symbol id="phone" viewBox="0 0 16 16"><path d="M3.2 1h3l1.3 3.4-1.8 1.2a8 8 0 0 0 4.6 4.6l1.2-1.8L15 9.8v3A2 2 0 0 1 13 15 12 12 0 0 1 1 3a2 2 0 0 1 2.2-2z" fill="currentColor"/></symbol>
  </defs>
</svg>

<div class="backdrop"></div>

<!-- Full newsletter -->
<article class="sheet sheet--full">
  <header class="masthead">
    <div class="masthead__mail"><svg><use href="#mail"/></svg>hello@vexaroll.com</div>
    <div class="brand"><span class="brand__dot"></span><span class="brand__name">Vexaroll</span></div>
    <div class="masthead__call"><svg><use href="#phone"/></svg>Call :555-014-2200</div>
  </header>
  <section class="hero" role="img" aria-label="Photo of a woman eating a fresh salad in a bright kitchen">
    <h1 class="hero__title">Helix Body Balance</h1>
  </section>
  <section class="factors">
    <h2 class="factors__title">Many Factors can lead to <span>Obesity</span></h2>
    <span class="pie__label pie__label--non">Non-Genetic Risk</span>
    <span class="pie__label pie__label--gen">Genetic Risk</span>
    <svg class="pie" viewBox="0 0 120 120">
      <circle cx="62" cy="62" r="53" fill="#17a99f"/>
      <path d="M56 56L56 2A54 54 0 0 0 14.4 21.6Z" fill="#3b3b3b" stroke="#fff" stroke-width="2"/>
      <text x="32" y="34" font-size="8" fill="#fff" font-family="Montserrat,sans-serif">14%</text>
      <text x="10" y="58" font-size="8" fill="#fff" font-family="Montserrat,sans-serif">86%</text>
    </svg>
    <ul class="checklist" style="color:var(--teal)">
      <li><svg><use href="#tick"/></svg><span style="color:#444">side effects of rx medicine</span></li>
      <li><svg><use href="#tick"/></svg><span style="color:#444">Hormonal Imbalances</span></li>
      <li><svg><use href="#tick"/></svg><span style="color:#444">Failure to control cravings</span></li>
      <li><svg><use href="#tick"/></svg><span style="color:#444">unhealthy diet</span></li>
      <li><svg><use href="#tick"/></svg><span style="color:#444">Lack of Appropriate Exercise</span></li>
    </ul>
    <p class="factors__note">Genetics Also Play A ROLE...up to 86% of Healthy Weight Levels is tied to Genetics</p>
  </section>
  <section class="markers">
    <div class="markers__figure" role="img" aria-label="Illustration of a leaping athletic figure"></div>
    <p class="markers__text">The Weight Management panel tests for five genetic markers that have been shown through research to be associated with an increased BMI. These genes are involved in different aspects of weight management.</p>
  </section>
  <section class="panel">
    <h2 class="panel__title">THE WEIGHT MANAGEMENT PANEL INCLUDES:</h2>
    <div class="panel__figure" role="img" aria-label="Illustration of a woman holding dumbbells and a basket of vegetables"></div>
    <span class="panel__label panel__label--meta">Metabolism regulation</span>
    <span class="panel__label panel__label--appetite">Appetite regulation and<br>craving frequency</span>
    <span class="panel__label panel__label--fat">Dietary fat sources and<br>fat utilization</span>
    <span class="panel__label panel__label--carb">Carbohydrate digestion<br>and physical activity</span>
    <span class="gene-dot gene-dot--mc4r">MC4R</span>
    <span class="gene-dot gene-dot--fto">FTO</span>
    <span class="gene-dot gene-dot--fabp2">FABP2</span>
    <span class="gene-dot gene-dot--adrb2">ADRB2</span>
    <span class="gene-dot gene-dot--sh2b1">SH2B1</span>
    <p class="panel__caption">Regulation of leptin and insulin</p>
  </section>
  <section class="benefits">
    <h2 class="benefits__title">Benefits Of Using Genetic Testing</h2>
    <p class="benefits__sub">You will receive:</p>
    <ul class="benefits__list">
      <li><svg><use href="#tick"/></svg>Personalize Diet &amp; Exercise Plan Designed for you based on your</li>
      <li><svg><use href="#tick"/></svg>Recipes that are tailored to maximize results</li>
    </ul>
    <div class="benefits__photo" role="img" aria-label="Photo of two women measuring their waists with a tape measure"></div>
  </section>
  <section class="invite">
    <p class="invite__lead">Let us help you personalize a Diet &amp; Exercise ratio<br>that fits you based on your genetic makeup!</p>
    <p class="invite__small">A more in-depth look at the weight management gene panel</p>
  </section>

  <table class="gene-table">
    <thead><tr><th class="col-gene">Gene</th><th class="col-type">Patient types</th><th class="col-plan">What to do</th></tr></thead>
    <tbody>
      <tr class="is-teal row-fto">
        <td class="col-gene">FTO</td>
        <td class="col-type">This person is hungry all the time, slow to</td>
        <td class="col-plan"><span class="plan__label">Diet :</span> Focus on portion control, eat slowly, chew food thoroughly and avoid unmonitored snacking. Choose low-starch vegetables and fruit with skins as the main source of carbs to increase fiber intake. Eat a higher amount of calories from protein which digests slowly, and a lower amount of calories from fat thus encouraging use
          <span class="plan__ex">Exercise :</span><span class="plan__ex-text">Moderate Level, 10-40 Minutes<br>5-7 days per week</span></td>
      </tr>
      <tr class="is-dark row-mc4r">
        <td class="col-gene">MC4R</td>
        <td class="col-type">This person loses weight more slowly than others. They are hungry all the time, slow to feel full and as a consequence crave high calorie foods. They have an increased chance of being insulin resistant. Increased chance of childhood obesity.</td>
        <td class="col-plan"><span class="plan__body"><span class="plan__label">Diet :</span> Eat small, portion controlled meals, with lots of fiber to increase feeling of satiety. Eat food with low calorie density like vegetables, and fruit and particularly green leafy salads, so if servings are large - it is with low calorie food. Limit fat intake because fat often has high calorie density.</span>
          <span class="plan__ex">Exercise :</span><span class="plan__ex-text">High-Intensity to burn off excess<br>glucose.</span></td>
      </tr>
      <tr class="is-teal row-fabp2">
        <td class="col-gene">FABP2</td>
        <td class="col-type">This is the patient that gains weight on the keto diet. They absorb saturated fats at a higher rate than those without the risk allele. This patient may be insulin resistant and struggle with high total and LDL cholesterol.</td>
        <td class="col-plan"><span class="plan__label">Diet :</span> Eat fiber rich meals with plenty of protein which breaks down slowly. Keep fat intake low. Use monounsaturated fats as opposed to saturated fats. Reduce simple carbohydrate intake such as refined foods and foods high in sugar, to control food cravings, prevent excess carbs from being stored as fat. Aim for 25 grams or more of fiber each day. Fiber is very important for FABP2 variant allele carriers through it's action on stabilizing blood sugar levels, insulin, and blood lipid levels.
          <span class="plan__ex">Exercise :</span><span class="plan__ex-text">High-Intensity to burn off excess<br>glucose.</span></td>
      </tr>
      <tr class="is-dark row-adrb2">
        <td class="col-gene">ADRB2</td>
        <td class="col-type">Susceptibility to obesity and asthma. Patients with this risk allele will often have trouble losing weight despite engaging in high intensity exercise.</td>
        <td class="col-plan"><span class="plan__label">Diet :</span> Low Carbohydrate Diet is very important for this allele type. Choose complex, low glycemic carbohydrates like whole grains, low starch vegetables, fruit with skins to increase fiber which helps control leptin, insulin levels, and fat in the bloodstream. Eat 20-30 grams of protein with each meal to ensure slower digestion time, maintain consistent supply of proteins for healthy muscle retention with exercise.
          <span class="plan__ex">Exercise :</span><span class="plan__ex-text">Low to moderate, 60 minutes per day. Although, exercise has has less impact on weight loss with the allele.</span></td>
      </tr>
      <tr class="is-teal row-sh2b1">
        <td class="col-gene">SH2B1</td>
        <td class="col-type">Intense hunger cravings, especially for sweets and high calorie foods, especially Sugar. Insulin resistance.</td>
        <td class="col-plan"><span class="plan__label">Diet :</span> Protein helps maintain the balance of insulin and leptin in the body and reduce spikes. Eating little and often helps improve leptin signaling. Choose complex low glycemic carbs like whole grains, low starch vegetables and fruit with skins to increase fiber, which helps control leptin, insulin levels, and fat in the blood stream. Ideally, eat carbohydrates with a glycemic index less than 55. Limit fat intake because fat often has high <b>calorie density.</b>
          <span class="plan__ex">Exercise :</span><span class="plan__ex-text">Low to moderate, 60 minutes per day. Although, exercise has has less impact on weight loss with the allele.</span></td>
      </tr>
    </tbody>
  </table>

  <section class="closing">
    <p class="closing__quote">“A goal without a plan is just a wish”</p>
    <div class="closing__bike" role="img" aria-label="Illustration of a woman riding an exercise bike"></div>
    <p class="closing__text">Talk to us about your<br>personalized plan today!</p>
  </section>
</article>

<!-- Short newsletter -->
<article class="sheet sheet--short">
  <header class="masthead">
    <div class="masthead__mail"><svg><use href="#mail"/></svg>hello@vexaroll.com</div>
    <div class="brand"><span class="brand__dot"></span><span class="brand__name">Vexaroll</span></div>
    <div class="masthead__call"><svg><use href="#phone"/></svg>Call :555-014-2200</div>
  </header>
  <section class="hero" role="img" aria-label="Photo of a woman eating a fresh salad in a bright kitchen">
    <h1 class="hero__title">Helix Body Balance</h1>
  </section>
  <section class="factors">
    <h2 class="factors__title">Many Factors can lead to <span>Obesity</span></h2>
    <span class="pie__label pie__label--non">Non-Genetic Risk</span>
    <span class="pie__label pie__label--gen">Genetic Risk</span>
    <svg class="pie" viewBox="0 0 120 120">
      <circle cx="62" cy="62" r="53" fill="#17a99f"/>
      <path d="M56 56L56 2A54 54 0 0 0 14.4 21.6Z" fill="#3b3b3b" stroke="#fff" stroke-width="2"/>
      <text x="32" y="34" font-size="8" fill="#fff" font-family="Montserrat,sans-serif">14%</text>
      <text x="10" y="58" font-size="8" fill="#fff" font-family="Montserrat,sans-serif">86%</text>
    </svg>
    <ul class="checklist" style="color:var(--teal)">
      <li><svg><use href="#tick"/></svg><span style="color:#444">side effects of rx medicine</span></li>
      <li><svg><use href="#tick"/></svg><span style="color:#444">Hormonal Imbalances</span></li>
      <li><svg><use href="#tick"/></svg><span style="color:#444">Failure to control cravings</span></li>
      <li><svg><use href="#tick"/></svg><span style="color:#444">unhealthy diet</span></li>
      <li><svg><use href="#tick"/></svg><span style="color:#444">Lack of Appropriate Exercise</span></li>
    </ul>
    <p class="factors__note">Genetics Also Play A ROLE...up to 86% of Healthy Weight Levels is tied to Genetics</p>
  </section>
  <section class="markers">
    <div class="markers__figure" role="img" aria-label="Illustration of a leaping athletic figure"></div>
    <p class="markers__text">The Weight Management panel tests for five genetic markers that have been shown through research to be associated with an increased BMI. These genes are involved in different aspects of weight management.</p>
  </section>
  <section class="panel">
    <h2 class="panel__title">THE WEIGHT MANAGEMENT PANEL INCLUDES:</h2>
    <div class="panel__figure" role="img" aria-label="Illustration of a woman holding dumbbells and a basket of vegetables"></div>
    <span class="panel__label panel__label--meta">Metabolism regulation</span>
    <span class="panel__label panel__label--appetite">Appetite regulation and<br>craving frequency</span>
    <span class="panel__label panel__label--fat">Dietary fat sources and<br>fat utilization</span>
    <span class="panel__label panel__label--carb">Carbohydrate digestion<br>and physical activity</span>
    <span class="gene-dot gene-dot--mc4r">MC4R</span>
    <span class="gene-dot gene-dot--fto">FTO</span>
    <span class="gene-dot gene-dot--fabp2">FABP2</span>
    <span class="gene-dot gene-dot--adrb2">ADRB2</span>
    <span class="gene-dot gene-dot--sh2b1">SH2B1</span>
    <p class="panel__caption">Regulation of leptin and insulin</p>
  </section>
  <section class="benefits">
    <h2 class="benefits__title">Benefits Of Using Genetic Testing</h2>
    <p class="benefits__sub">You will receive:</p>
    <ul class="benefits__list">
      <li><svg><use href="#tick"/></svg>Personalize Diet &amp; Exercise Plan Designed for you based on your</li>
      <li><svg><use href="#tick"/></svg>Recipes that are tailored to maximize results</li>
    </ul>
    <div class="benefits__photo" role="img" aria-label="Photo of two women measuring their waists with a tape measure"></div>
  </section>
  <section class="invite">
    <p class="invite__lead">Let us help you personalize a Diet &amp; Exercise ratio<br>that fits you based on your genetic makeup!</p>
    <p class="invite__small">A more in-depth look at the weight management gene panel</p>
  </section>
  <section class="closing">
    <p class="closing__quote">“A goal without a plan is just a wish”</p>
    <div class="closing__bike" role="img" aria-label="Illustration of a woman riding an exercise bike"></div>
    <p class="closing__text">Talk to us about your<br>personalized plan today!</p>
  </section>
</article>
</body>
</html>
```